Please look at my website to get a better understanding of my business: www.perovatu.com
This business is about Life Coaching for Families, couples, teenagers and individuals. I work more w parents of teenagers (as well as teenagers) but not so much with young kids.
The card should be fun, not too busy, with a sense of flow and playfulness. Warm colors, artistic style (can have a family sculpture, paining or a picture in it). Basic information about myself and my company

Reason: I extended my due date for next Tuesday, November 13th. Please summit new designs if you haven't done so, and for those who submitted, thank you so much for your time and effort. I will make a decision next Tues, and will contact you if I need to revise some items. Much thanks to you all! Orla

Families, parents, teenagers, couples, individuals.

Business

• Business name: PeRoVaTu! Hearth Circle Life Coaching
My name: Orla Bekwith, RMTQ
Description of my work: Tri-Mode life coach
Tel: 555-304-7719
Website: www.perovatu.com
• Family sculpture, abstract painting or a picture, or simply a nice background w/out a picture added.
• Corporate feeling, cold colors, corporate symbols. no Sunset, or picture of families on the beach.
Don't include bar-code (from uploaded file 1, it is only the designer to find out more about my website).

```html
<!DOCTYPE html>
<html lang="en">
<head>
<meta charset="utf-8">
<title>Perovatu – Hearth Circle Life Coaching</title>
<link rel="stylesheet" href="https://fonts.googleapis.com/css2?family=Tinos:ital,wght@0,400;0,700;1,400;1,700&display=swap">
<style>
  :root {
    --paper: #ffffff;
    --brand-red: #7a1010;
    --ink: #2b2b2b;
    --ink-soft: #3a3a3a;
    --ochre: #d49a45;
    --rust: #b95a18;
    --vermilion: #c8380f;
    --dot-orange: #eab48a;
    --silhouette: #cfcfcf;
  }
  * { margin: 0; padding: 0; box-sizing: border-box; }
  html, body { width: 1200px; height: 777px; overflow: hidden; background: var(--paper); }
  .card {
    position: relative;
    width: 1200px;
    height: 777px;
    background: var(--paper);
    font-family: "Tinos", "Times New Roman", serif;
    overflow: hidden;
  }
  .color-tabs {
    position: absolute;
    top: 0;
    left: 722px;
    display: flex;
  }
  .color-tabs span { display: block; width: 140px; height: 72px; }
  .color-tabs .tab-ochre { background: var(--ochre); }
  .color-tabs .tab-rust { background: var(--rust); }
  .color-tabs .tab-vermilion { background: var(--vermilion); }

  .dot-field {
    position: absolute;
    left: 0;
    top: 250px;
    width: 1200px;
    height: 527px;
    background:
      radial-gradient(ellipse 520px 300px at 20% 80%, rgba(234,180,138,0.55), rgba(234,180,138,0) 70%),
      radial-gradient(ellipse 500px 280px at 70% 40%, rgba(234,180,138,0.35), rgba(234,180,138,0) 70%);
  }
  .family-figure {
    position: absolute;
    left: 788px;
    top: 233px;
    width: 412px;
    height: 544px;
    background: linear-gradient(180deg, rgba(190,190,190,0.55) 0%, rgba(215,215,215,0.45) 60%, rgba(235,235,235,0.3) 100%);
  }

  .brand-name {
    position: absolute;
    left: 60px;
    top: 52px;
    font-size: 96px;
    font-weight: 700;
    line-height: 1;
    color: var(--ink);
  }
  .brand-tagline {
    position: absolute;
    right: 59px;
    top: 180px;
    font-size: 48px;
    font-weight: 700;
    font-style: italic;
    line-height: 1;
    color: var(--brand-red);
  }
  .coach-name {
    position: absolute;
    left: 0;
    width: 1200px;
    top: 360px;
    text-align: center;
    font-size: 64px;
    font-weight: 700;
    line-height: 1;
    color: var(--ink);
  }
  .coach-role {
    position: absolute;
    left: 0;
    width: 1200px;
    top: 443px;
    text-align: center;
    font-size: 36px;
    font-style: italic;
    line-height: 1;
    color: var(--ink-soft);
  }
  .contact-line {
    position: absolute;
    left: 54px;
    top: 658px;
    font-size: 64px;
    line-height: 1;
    color: var(--ink);
    white-space: nowrap;
  }
</style>
</head>
<body>
  <div class="card">
    <div class="dot-field" role="img" aria-label="Soft orange halftone dot pattern fading across the card"></div>
    <div class="family-figure" role="img" aria-label="Grey silhouette of a family: two parents and a child"></div>

    <div class="color-tabs" aria-hidden="true">
      <span class="tab-ochre"></span>
      <span class="tab-rust"></span>
      <span class="tab-vermilion"></span>
    </div>

    <h1 class="brand-name">Perovatu</h1>
    <p class="brand-tagline">Hearth Circle Life Coaching</p>

    <h2 class="coach-name">Orla BEKWITH, RMTQ</h2>
    <p class="coach-role">Tri-Mode life coach</p>

    <p class="contact-line">tel: 555-304-7719 • www.perovatu.com</p>
  </div>
</body>
</html>
```